Integrated Health Clinic brochure

We need a brochure designed to highlight the services that we offer at the integrated clinic. Please see "Our Services" of our website for description of services to be added to the brochure except for Acupuncture, which is described below:

"Acupuncture is an ancient Chinese methodology that has been proven to be very effective in many health issues, particularly in relieving pain. It involves the stimulation of acupuncture points on the body to regain the natural balance of the body. Medical Acupuncture is effective in treating a wide variety of conditions including: headaches, neck and back pains, carpal tunnel syndrome, fibromyalgia, asthma, allergies, sinus problems, digestive disorders and many others."

our motto "Relieve, Rejuvenate, Renew"

Services we provide:
Chiropractic
Physiotherapy
Family counselling
Massage Therapy
Acupuncture
Osteopath

Colors are blue and green.

See our website www.solvarahealth.ca

```html
<!DOCTYPE html>
<html lang="en">
<head>
<meta charset="utf-8">
<title>Our Services – Solvara Health Brochure</title>
<link href="https://fonts.googleapis.com/css2?family=Open+Sans:wght@400;600&family=Advent+Pro:wght@400&display=swap" rel="stylesheet">
<style>
  :root {
    --green: #7dc242;
    --green-dark: #5fa82c;
    --blue: #1f8fd6;
    --text: #222222;
    --grey: #6b6b6b;
    --navy: #2a3446;
    --paper: #ffffff;
    --photo-light: #e4e7ea;
    --photo-mid: #9aa6b4;
    --photo-dark: #3d3a3a;
    --photo-warm: #b49a86;
  }
  * { margin: 0; padding: 0; box-sizing: border-box; }
  html, body { width: 848px; height: 1200px; overflow: hidden; background: var(--paper); }
  body { font-family: "Open Sans", Arial, sans-serif; color: var(--text); }
  .page { position: relative; width: 848px; height: 1200px; overflow: hidden; background: var(--paper); }

  .site-line { position: absolute; left: 54px; top: 14px; font-size: 17px; color: var(--grey); font-family: Arial, "Open Sans", sans-serif; }
  .site-line .site-url { color: var(--green); }

  .title-band { position: absolute; left: 0; top: 47px; }
  .page-title { position: absolute; left: 54px; top: 48px; font-size: 44px; font-weight: 400; color: #fff; letter-spacing: 0.5px; line-height: 60px; }

  .service-text { position: absolute; font-size: 12.6px; line-height: 20.2px; text-align: justify; }
  .service-text .service-name { color: var(--green); font-size: 26px; font-weight: 400; line-height: 20px; }
  .counselling-text { left: 51px; top: 125px; width: 391px; }
  .acupuncture-text { left: 60px; top: 713px; width: 382px; }
  .acupuncture-text .service-name { font-size: 25px; }

  .photo { position: absolute; border: 1px solid #cfcfcf; }
  .photo-family { left: 467px; top: 125px; width: 330px; height: 348px;
    background: linear-gradient(160deg, var(--photo-light) 0%, #d6dde4 45%, var(--photo-mid) 80%, #5a7090 100%); }
  .photo-acupuncture { left: 467px; top: 715px; width: 330px; height: 347px;
    background: radial-gradient(circle at 35% 50%, var(--photo-warm) 0%, #6e5a50 40%, var(--photo-dark) 75%, #2a2828 100%); }

  .fees-heading { position: absolute; left: 51px; top: 480px; font-family: "Advent Pro", "Open Sans", sans-serif; font-size: 23px; color: var(--green); }
  .fees-list { position: absolute; left: 51px; top: 523px; list-style: none; font-size: 15.4px; line-height: 22.5px; }
  .fees-list li::before { content: "*"; color: var(--green); display: inline-block; width: 24px; }
  .fee-label { color: var(--blue); }
  .fee-price { color: var(--text); }

  .divider { position: absolute; left: 51px; width: 746px; height: 9px; top: 645px; border-top: 2px solid var(--green); border-bottom: 1px solid var(--green); }

  .footer-band { position: absolute; left: 0; bottom: 0; width: 848px; height: 39px; background: var(--navy); }
  .footer-swoosh { position: absolute; left: 716px; top: 1142px; }
  .page-number { position: absolute; left: 800px; top: 1166px; color: #fff; font-size: 20px; font-family: Georgia, serif; }
</style>
</head>
<body>
<div class="page">
  <p class="site-line">Visit our website: <span class="site-url">www.solvarahealth.ca/</span></p>

  <svg class="title-band" width="570" height="62" viewBox="0 0 570 62">
    <polygon points="0,0 438,0 500,62 0,62" fill="#7dc242"/>
    <polygon points="450,0 500,0 562,62 512,62" fill="#7dc242"/>
  </svg>
  <h1 class="page-title">Our Services</h1>

  <p class="service-text counselling-text"><span class="service-name">FAMILY COUNSELLING</span> Our relationships with ourselves and our loved ones is an integrated part of our overall well being and can often influence our bodies physically. Our registered Social Work practitioner assists clients in handling individual, family, emotional or educational issues in a professional and confidential manner. Whether it is marital issues, parenting concerns or individual matters, a chat with our counsellor can ease your stress and put you on the right path.</p>

  <div class="photo photo-family" role="img" aria-label="Photo of a family in a counselling session with a counsellor"></div>

  <h2 class="fees-heading">Family counselling fees (Covered by most Extended Health Plans)</h2>
  <ul class="fees-list">
    <li><span class="fee-label">Individual sessions</span> <span class="fee-price">$65</span> <span class="fee-label">to</span> <span class="fee-price">$100</span></li>
    <li><span class="fee-label">Three 60 mins package</span> <span class="fee-price">$210</span></li>
    <li><span class="fee-label">Psychological Educational Assessments (Gifted Student Test) from</span> <span class="fee-price">$1,500</span></li>
    <li><span class="fee-label">Psychological Educational Assessments (Learning Disability Test) from</span> <span class="fee-price">$1,500</span></li>
  </ul>

  <div class="divider"></div>

  <p class="service-text acupuncture-text"><span class="service-name">Acupuncture</span> is an ancient Chinese methodology that has been proven to be very effective in many health issues, particularly in relieving pain. It involves the stimulation of acupuncture points on the body to regain the natural balance of the body. Medical Acupuncture is effective in treating a wide variety of conditions including: headaches, neck and back pains, carpal tunnel syndrome, fibromyalgia, asthma, allergies, sinus problems, digestive disorders and many others.”</p>

  <div class="photo photo-acupuncture" role="img" aria-label="Photo of a practitioner placing acupuncture needles on a patient"></div>

  <div class="footer-band"></div>
  <svg class="footer-swoosh" width="90" height="58" viewBox="0 0 90 58">
    <path d="M2,58 C20,30 50,12 88,10 L84,22 C56,24 34,38 22,58 Z" fill="#7dc242"/>
  </svg>
  <span class="page-number">3</span>
</div>
</body>
</html>
```